" Trabalhamos visitando nossos clientes no porta a portas, clientes esses com escolas, colégios e creches particulares e prefeituras. Fora a venda particular, participamos de licitações em prefeituras. "

```html
<!DOCTYPE html>
<html lang="pt">
<head>
<meta charset="utf-8">
<title>Sable Crest Comercial — Pasta institucional</title>
<link href="https://fonts.googleapis.com/css2?family=Montserrat:wght@300;400;600&display=swap" rel="stylesheet">
<style>
  :root {
    --bg: #ecebe6;
    --ink-dark: #2c3238;
    --ink-darker: #23282d;
    --paper: #ffffff;
    --gold: #c9a13a;
    --text-grey: #5c6166;
    --label-grey: #8a8f94;
    --strip: #e3c66a;
  }
  * { margin: 0; padding: 0; box-sizing: border-box; }
  html, body { width: 1200px; height: 1200px; overflow: hidden; }
  body {
    background: var(--bg);
    font-family: "Montserrat", sans-serif;
    position: relative;
  }

  /* Open folder: inside left flap + inside right panel */
  .folder-inside-left {
    position: absolute; left: 120px; top: 355px;
    width: 288px; height: 593px;
    background: var(--paper);
    box-shadow: 0 2px 8px rgba(0,0,0,0.08);
  }
  .folder-inside-right {
    position: absolute; left: 408px; top: 355px;
    width: 312px; height: 593px;
    background: var(--ink-dark);
    overflow: hidden;
  }

  .brand {
    display: flex; flex-direction: column; align-items: center;
    gap: 6px; text-align: center;
  }
  .brand-name {
    font-weight: 300;
    letter-spacing: 0.14em;
    text-transform: uppercase;
    color: var(--gold);
    line-height: 1.2;
  }
  .brand-mark {
    width: 14px; height: 14px; background: var(--gold);
  }
  .folder-inside-left .brand {
    position: absolute; left: 0; right: 0; top: 250px;
  }
  .folder-inside-left .brand-name { font-size: 17px; }

  /* Letterhead sheet */
  .letterhead {
    position: absolute; left: 19px; top: 17px;
    width: 269px; height: 560px;
    background: var(--paper);
    padding: 22px 22px 0 30px;
  }
  .letterhead-strip {
    position: absolute; left: 0; top: 0;
    width: 12px; height: 262px; background: var(--strip);
  }
  .letterhead-brand {
    font-size: 9px; font-weight: 300; letter-spacing: 0.14em;
    text-transform: uppercase; color: var(--gold);
    margin-left: 14px; margin-bottom: 38px;
  }
  .letterhead-body {
    font-size: 6.3px; line-height: 1.75; color: var(--text-grey);
  }
  .letterhead-body h2 {
    font-size: 7px; font-weight: 600; color: var(--ink-dark);
    margin-bottom: 8px;
  }
  .letterhead-body p { margin-bottom: 8px; }

  .pocket {
    position: absolute; left: 0; top: 0; width: 312px; height: 593px;
  }

  /* Closed folder cover */
  .folder-cover {
    position: absolute; left: 756px; top: 355px;
    width: 336px; height: 593px;
    background: var(--ink-dark);
  }
  .folder-cover .brand {
    position: absolute; left: 0; right: 0; top: 225px;
  }
  .folder-cover .brand-name { font-size: 18px; }
</style>
</head>
<body>

  <section class="folder-inside-left">
    <div class="brand">
      <span class="brand-mark"></span>
      <span class="brand-name">Sable Crest Comercial</span>
    </div>
  </section>

  <section class="folder-inside-right">
    <article class="letterhead">
      <span class="letterhead-strip"></span>
      <div class="letterhead-brand">Sable Crest Comercial</div>
      <div class="letterhead-body">
        <h2>Prezado cliente,</h2>
        <p>Agradecemos a confiança em nosso trabalho. Atendemos escolas, colégios e creches particulares com materiais de qualidade, entrega rápida e atendimento próximo em cada visita.</p>
        <p>Também participamos de licitações em prefeituras, oferecendo propostas claras, prazos cumpridos e suporte completo do pedido à entrega final.</p>
        <p>Seguimos à disposição para novas parcerias e para apresentar nosso catálogo completo.</p>
        <p>Atenciosamente,</p>
      </div>
    </article>

    <svg class="pocket" viewBox="0 0 312 593" aria-hidden="true">
      <path d="M0 300 L40 300 Q60 300 70 320 L90 360 L312 250 L312 593 L0 593 Z" fill="#262b30"/>
      <path d="M0 300 L40 300 Q60 300 70 320 L90 360 L312 250" fill="none" stroke="#1c2024" stroke-width="1.5"/>
      <path d="M0 400 L312 300 L312 593 L0 593 Z" fill="var(--ink-darker)" opacity="0.35"/>
    </svg>
  </section>

  <section class="folder-cover">
    <div class="brand">
      <span class="brand-mark"></span>
      <span class="brand-name">Sable Crest Comercial</span>
    </div>
  </section>

</body>
</html>
```